Brightway Inc. Business Card Design

Brightway Inc. is in search of a great clean design for our business cards!

Looking to incorporate our full logo and watermark on side one (however, I am open to having the text and watermark separated within the design.)

On side two, I am looking to have contact information (Name, Position, Phone #, Email, Website (www.thebrightway.ca). Can have the logo and/or watermark as part of the design if applicable.

Please add tagline "Where Shine Counts" on either side 1 or 2. This tagline can be in a sans serif, serif or cursive font as long as it compliments overall design. Capitalization can be title or sentence case depending on how it fits within the design.

Get creative!! Looking for a clean, crisp, premium design! Looking for a glossy card finish with spot UV features when printed. Cards will also be printed with rounded corners. Standard dimensions (3.5 x 2).

Target Market(s)

B2B - primary clients are business owners or property management corporations. (residential jobs are few and far between)

Industry/Entity Type

Business

Contact Information for Business Card

- clean, crisp design
- double sided
- spot UV accents and glossy finish upon printing
- standard business card size (3.5 x 2) with rounded corners
- please see project description for requirements per side

Font styles to use
Sans Serif

Requirements
Must have
• - adequate bleeds with print ready files
• - cohesive design elements between side 1 & 2
• - spot UV elements (can be on both sides or just one, use your discretion)
• - colour pallet should match the logo file provided
• - incorporate tagline "where shine counts" (this tagline can be in a serif or sans serif font as long as it is complimentary to the overall design.
Nice to have
• - Premium elements with a clean design
Should not have
• - Please omit cartoon or whimsical like designs, think premium.
• - Colours should not stray from the pallet of the provided logo.

```html
<!DOCTYPE html>
<html lang="en">
<head>
<meta charset="utf-8">
<title>Brightway Inc. Business Card</title>
<link href="https://fonts.googleapis.com/css2?family=Open+Sans:wght@700;800&family=Roboto:wght@400;500&display=swap" rel="stylesheet">
<style>
  :root {
    --teal: #10b3b5;
    --navy: #1f2755;
    --ink: #4a4a4a;
    --paper: #f4f4f4;
    --backdrop: #2b2b2b;
    --white: #ffffff;
  }
  html, body {
    margin: 0;
    width: 1200px;
    height: 960px;
    overflow: hidden;
    background: var(--backdrop);
    font-family: "Roboto", Arial, sans-serif;
  }
  .card {
    position: absolute;
    width: 600px;
    height: 343px;
    border-radius: 20px;
    overflow: hidden;
  }
  .card--front { left: 314px; top: 113px; background: var(--paper); }
  .card--back { left: 311px; top: 472px; background: var(--teal); }

  .brand-name {
    position: absolute;
    left: 54px;
    top: 48px;
    margin: 0;
    font-family: "Open Sans", Arial, sans-serif;
    font-weight: 800;
    font-size: 40px;
    letter-spacing: -1px;
    white-space: nowrap;
    color: var(--navy);
  }
  .address {
    position: absolute;
    left: 54px;
    top: 152px;
    margin: 0;
    font-size: 14.5px;
    line-height: 18px;
    color: var(--ink);
    font-style: normal;
  }
  .contact-list {
    position: absolute;
    left: 54px;
    top: 198px;
    margin: 0;
    padding: 0;
    list-style: none;
    font-size: 14.5px;
    color: var(--ink);
  }
  .contact-list li {
    display: flex;
    align-items: center;
    height: 19px;
  }
  .contact-list svg { width: 14px; height: 14px; margin-right: 8px; fill: var(--teal); }
  .person {
    position: absolute;
    right: 48px;
    top: 190px;
    text-align: right;
    white-space: nowrap;
  }
  .person__name {
    margin: 0;
    font-weight: 500;
    font-size: 21px;
    color: var(--teal);
  }
  .person__role {
    margin: 4px 0 0;
    font-weight: 500;
    font-size: 14.5px;
    color: var(--navy);
  }
  .footer-band {
    position: absolute;
    left: 0;
    bottom: 0;
    width: 600px;
    height: 28px;
  }
  .website {
    position: absolute;
    left: 54px;
    bottom: 6px;
    margin: 0;
    font-size: 13px;
    letter-spacing: 5.5px;
    white-space: nowrap;
    color: var(--white);
  }

  .back-lockup {
    position: absolute;
    left: 60px;
    top: 304px;
    width: 270px;
    transform-origin: 0 0;
    transform: rotate(-90deg);
    white-space: nowrap;
  }
  .back-lockup__name {
    margin: 0;
    font-family: "Open Sans", Arial, sans-serif;
    font-weight: 800;
    font-size: 31px;
    letter-spacing: -0.5px;
    line-height: 38px;
    color: var(--white);
  }
  .back-lockup__tagline {
    margin: 2px 0 0;
    font-size: 12.5px;
    letter-spacing: 5px;
    line-height: 18px;
    color: var(--white);
  }
</style>
</head>
<body>
  <section class="card card--front" aria-label="Front of card">
    <h1 class="brand-name">BRIGHTWAY INC.</h1>
    <address class="address">412 Harbourview Road<br>Halifax, Nova Scotia B3K 2L9</address>
    <ul class="contact-list">
      <li><svg viewBox="0 0 24 24" aria-hidden="true"><path d="M6.6 10.8a15.1 15.1 0 0 0 6.6 6.6l2.2-2.2a1 1 0 0 1 1-.25 11.4 11.4 0 0 0 3.6.57 1 1 0 0 1 1 1V20a1 1 0 0 1-1 1A17 17 0 0 1 3 4a1 1 0 0 1 1-1h3.5a1 1 0 0 1 1 1c0 1.25.2 2.45.57 3.57a1 1 0 0 1-.25 1z"/></svg>902 555 0148</li>
      <li><svg viewBox="0 0 24 24" aria-hidden="true"><path d="M7 1h10a2 2 0 0 1 2 2v18a2 2 0 0 1-2 2H7a2 2 0 0 1-2-2V3a2 2 0 0 1 2-2zm0 3v14h10V4z"/></svg>902 555 0173</li>
      <li><svg viewBox="0 0 24 24" aria-hidden="true"><path d="M6 2h10l2 2v4H6zM3 9h18a2 2 0 0 1 2 2v7h-4v4H5v-4H1v-7a2 2 0 0 1 2-2zm4 8v3h10v-3z"/></svg>902 555 0196</li>
      <li><svg viewBox="0 0 24 24" aria-hidden="true"><path d="M2 5h20v14H2zm2 2v.5l8 5 8-5V7zm0 2.8V17h16V9.8l-8 5z"/></svg>dana@thebrightway.ca</li>
    </ul>
    <div class="person">
      <p class="person__name">DANA WHITFIELD</p>
      <p class="person__role">CEO/FOUNDER</p>
    </div>
    <svg class="footer-band" viewBox="0 0 600 28" aria-hidden="true">
      <polygon points="0,0 432,0 422,28 0,28" fill="var(--teal)"/>
      <polygon points="438,0 600,0 600,28 427,28" fill="var(--navy)"/>
    </svg>
    <p class="website">www.thebrightway.ca</p>
  </section>

  <section class="card card--back" aria-label="Back of card">
    <div class="back-lockup">
      <p class="back-lockup__name">BRIGHTWAY INC.</p>
      <p class="back-lockup__tagline">Where Shine Counts</p>
    </div>
  </section>
</body>
</html>
```